Service Menu refresh 2018 Update of menu pricing

We currently have service menus as attached. We will be updating our look via our homepage image, our service menu and our in-house beverage and treatment menu.
We are a natural and sustainable hair salon group and moving more towards head spa which consists of treatments, beauty, tanning as well as your traditional hair services. Our imagery needs to reflect our efforts in spa treatments in the hair and scalp area and use natural materials and colours reflecting sustainability.
Velin is the brand we stock and promote.

Target Market(s)

Men or women interesting in personal maintenance with natural and organic products and using sustainable practises

Industry/Entity Type

Hair And Beauty

Font styles to use
Sans Serif
Other font styles liked:
• Arial or Helvetica

Colors
9acb3c
abd037
cadf82
ffffff

Requirements
Must have
• Name on the front cover, locations on back cover
Nice to have
• Prestige feel, reflect male and female clients
Should not have
• Bold artificial writing or any type of cartoon images.
• Same images as existing menu.

```html
<!DOCTYPE html>
<html lang="en">
<head>
<meta charset="utf-8">
<title>Quillow Hair Salons – Service Menu</title>
<link href="https://fonts.googleapis.com/css2?family=Open+Sans:wght@300;400;600&display=swap" rel="stylesheet">
<style>
  :root{
    --leaf:#7dc142;
    --leaf-dark:#436a4a;
    --leaf-soft:#9acb3c;
    --ink:#1e1e1e;
    --text:#555;
    --price:#4a4a4a;
    --paper:#f3f3f3;
    --page:#e4e4e2;
    --white:#ffffff;
  }
  *{box-sizing:border-box;margin:0;padding:0}
  html,body{width:1075px;height:1200px;overflow:hidden}
  body{background:var(--page);font-family:"Open Sans",Arial,sans-serif;color:var(--text);position:relative}

  .card{position:absolute;left:80px;width:940px;height:510px;background:var(--paper);box-shadow:0 3px 10px rgba(0,0,0,.25);overflow:hidden}
  .card--front{top:51px}
  .card--back{top:624px}

  /* front cover */
  .front-art{position:absolute;left:0;top:0;width:520px;height:510px}
  .brand{position:absolute;display:flex;align-items:center;gap:12px;color:var(--ink);font-weight:400;white-space:nowrap}
  .brand__dot{display:block;border-radius:50%;background:var(--leaf);flex:none}
  .card--front .brand{left:473px;top:40px;font-size:38px;letter-spacing:-.5px}
  .card--front .brand__dot{width:56px;height:56px}

  .locations{position:absolute;left:555px;top:106px;list-style:none}
  .location{height:71px}
  .location__name{display:flex;align-items:center;gap:8px;font-size:16.5px;color:var(--ink);text-transform:uppercase;margin-left:-8px;line-height:22px}
  .location__name svg{width:11px;height:14px;flex:none}
  .location__line{font-size:12.5px;line-height:18px;color:var(--text)}
  .location__line b{font-weight:600;color:var(--ink)}
  .web-bar{position:absolute;left:602px;top:462px;width:338px;height:37px;background:var(--leaf);border-radius:18px 0 0 18px;color:var(--white);font-size:15.5px;letter-spacing:.3px;display:flex;align-items:center;padding-left:20px}

  /* back cover */
  .back-art{position:absolute;right:0;top:0;width:380px;height:510px;background:radial-gradient(ellipse at 60% 45%,#dfe3dc 0%,#e7eae4 45%,rgba(242,242,242,0) 80%)}
  .card--back .brand{left:34px;top:22px;font-size:34px;letter-spacing:-.5px}
  .card--back .brand__dot{width:66px;height:66px}

  .note{position:absolute;left:492px;top:29px;width:404px;height:64px;background:var(--leaf);color:var(--white);font-size:10.5px;line-height:13px;padding:7px 8px}

  .menu{position:absolute;width:398px}
  .menu--left{left:28px}
  .menu--right{left:492px}
  .section{position:absolute;left:0;width:398px}
  .section__head{display:grid;height:27px;border-bottom:1.5px solid var(--leaf-soft);font-size:16.5px;color:var(--ink);text-transform:uppercase;align-items:center;margin-bottom:7px}
  .row{display:grid;height:13px;align-items:center;font-size:10.5px;line-height:13px;white-space:nowrap}
  .row--cat{font-size:12px;text-transform:uppercase}
  .row--small{font-size:10px}
  .menu--left .section__head,.menu--left .row{grid-template-columns:261px 34px 42px 33px 1fr}
  .menu--right .section__head,.menu--right .row{grid-template-columns:261px 34px 43px 34px 1fr}
  .price{color:var(--price);font-size:9.5px;text-transform:none}
</style>
</head>
<body>

<section class="card card--front" aria-label="Front cover">
  <svg class="front-art" viewBox="0 0 520 510">
    <defs>
      <linearGradient id="hairTone" x1="0" y1="0" x2="1" y2="1">
        <stop offset="0" stop-color="#d9cbbd"/>
        <stop offset=".5" stop-color="#b9a591"/>
        <stop offset="1" stop-color="#e8e0d6"/>
      </linearGradient>
    </defs>
    <path role="img" aria-label="Photo of a woman in profile with long, glossy, straight blonde hair" d="M0 0 H405 C470 150,480 380,376 510 H0 Z" fill="url(#hairTone)"/>
    <path d="M405 0 H420 C500 160,500 380,460 510 H376 C480 380,470 150,405 0 Z" fill="var(--leaf)"/>
    <path d="M420 0 H436 C515 170,520 380,478 510 H460 C500 380,500 160,420 0 Z" fill="var(--leaf-dark)"/>
  </svg>

  <div class="brand"><span class="brand__dot"></span>Quillow Hair Salons</div>

  <ul class="locations">
    <li class="location">
      <div class="location__name"><svg viewBox="0 0 11 14"><path d="M5.5 0A5.5 5.5 0 0 0 0 5.5C0 9 5.5 14 5.5 14S11 9 11 5.5A5.5 5.5 0 0 0 5.5 0Zm0 7.6a2.1 2.1 0 1 1 0-4.2 2.1 2.1 0 0 1 0 4.2Z" fill="var(--leaf)"/></svg>Hollowmere</div>
      <div class="location__line">Harbour Lane, Hollowmere Plaza, 4101</div>
      <div class="location__line"><b>p:</b> 07 5550 1184 &nbsp;&nbsp;<b>e:</b> hollowmere@quillowhair.com.au</div>
    </li>
    <li class="location">
      <div class="location__name"><svg viewBox="0 0 11 14"><path d="M5.5 0A5.5 5.5 0 0 0 0 5.5C0 9 5.5 14 5.5 14S11 9 11 5.5A5.5 5.5 0 0 0 5.5 0Zm0 7.6a2.1 2.1 0 1 1 0-4.2 2.1 2.1 0 0 1 0 4.2Z" fill="var(--leaf)"/></svg>Ferndale Park</div>
      <div class="location__line">Wattle Road, Ferndale Park Centre, 4102</div>
      <div class="location__line"><b>p:</b> 07 5550 2273 &nbsp;&nbsp;<b>e:</b> ferndale@quillowhair.com.au</div>
    </li>
    <li class="location">
      <div class="location__name"><svg viewBox="0 0 11 14"><path d="M5.5 0A5.5 5.5 0 0 0 0 5.5C0 9 5.5 14 5.5 14S11 9 11 5.5A5.5 5.5 0 0 0 5.5 0Zm0 7.6a2.1 2.1 0 1 1 0-4.2 2.1 2.1 0 0 1 0 4.2Z" fill="var(--leaf)"/></svg>Kestrel Bay</div>
      <div class="location__line">Marsh Road, Kestrel Bay Shopping Centre, 4103</div>
      <div class="location__line"><b>p:</b> 07 5550 3391 &nbsp;&nbsp;<b>e:</b> kestrelbay@quillowhair.com.au</div>
    </li>
    <li class="location">
      <div class="location__name"><svg viewBox="0 0 11 14"><path d="M5.5 0A5.5 5.5 0 0 0 0 5.5C0 9 5.5 14 5.5 14S11 9 11 5.5A5.5 5.5 0 0 0 5.5 0Zm0 7.6a2.1 2.1 0 1 1 0-4.2 2.1 2.1 0 0 1 0 4.2Z" fill="var(--leaf)"/></svg>Northbrook</div>
      <div class="location__line">Juniper Street, Northbrook Square, 4104</div>
      <div class="location__line"><b>p:</b> 07 5550 4426 &nbsp;&nbsp;<b>e:</b> hollowmere@quillowhair.com.au</div>
    </li>
    <li class="location">
      <div class="location__name"><svg viewBox="0 0 11 14"><path d="M5.5 0A5.5 5.5 0 0 0 0 5.5C0 9 5.5 14 5.5 14S11 9 11 5.5A5.5 5.5 0 0 0 5.5 0Zm0 7.6a2.1 2.1 0 1 1 0-4.2 2.1 2.1 0 0 1 0 4.2Z" fill="var(--leaf)"/></svg>Ridgeview Womens Hospital</div>
      <div class="location__line">Ashwood St, Ridgeview, 4105</div>
      <div class="location__line"><b>p:</b> 07 5550 5517 &nbsp;&nbsp;<b>e:</b> ridgeview@quillowhair.com.au</div>
    </li>
  </ul>

  <div class="web-bar">WWW.QUILLOWHAIR.COM.AU</div>
</section>

<section class="card card--back" aria-label="Service menu">
  <div class="back-art" role="img" aria-label="Faint line illustration of tropical leaves and botanical foliage"></div>

  <div class="brand"><span class="brand__dot"></span>Quillow Hair Salons</div>

  <div class="note">*Pricing is indicative of average products used and time taken for each service.<br>You will always receive a firm price after your consultation.<br>S to the jaw line | M to the collarbone | L to the bra strap | Xl past bra strap</div>

  <div class="menu menu--left">
    <div class="section" style="top:119px">
      <div class="section__head"><span>Cut &amp; Blow-dry</span><span>S</span><span>M</span><span>L</span><span>XL</span></div>
      <div class="row row--cat"><span>Ladies</span><span class="price">$77</span><span class="price">$88</span><span class="price">$99</span><span class="price">$110</span></div>
      <div class="row row--cat"><span>Fringe</span></div>
      <div class="row row--small"><span>Trim</span><span class="price">$25</span></div>
      <div class="row row--small"><span>Restyle</span><span class="price">$35</span></div>
      <div class="row row--cat"><span>Mens</span></div>
      <div class="row row--small"><span>Single blade clipper</span><span class="price">$28</span></div>
      <div class="row row--small"><span>Style cut</span><span class="price">$42</span></div>
      <div class="row row--cat"><span>Children</span></div>
      <div class="row row--small"><span>10 and under</span><span class="price">$24</span></div>
      <div class="row row--small"><span>11-16 Male</span><span class="price">$32</span></div>
      <div class="row row--small"><span>11-16 Female</span><span class="price">$48</span></div>
      <div class="row row--small"><span>add a wash</span><span class="price">$5</span></div>
      <div class="row row--cat"><span>Blowdry</span><span class="price">$47</span><span class="price">$57</span><span class="price">$67</span><span class="price">$77</span></div>
      <div class="row row--small"><span>Shampoo &amp; dry off</span><span class="price">$25</span></div>
    </div>
    <div class="section" style="top:346px">
      <div class="section__head"><span>Treatments</span></div>
      <div class="row row--small"><span>Deep treatment</span><span class="price">$35</span></div>
      <div class="row row--small"><span>Head.Spa ritual</span><span class="price">$65</span></div>
    </div>
    <div class="section" style="top:419px">
      <div class="section__head"><span>Upstile</span></div>
      <div class="row row--small"><span>45 minutes</span><span class="price">$85</span></div>
      <div class="row row--small"><span>60 minutes</span><span class="price">$120</span></div>
    </div>
  </div>

  <div class="menu menu--right">
    <div class="section" style="top:119px">
      <div class="section__head"><span>Colour</span><span>S</span><span>M</span><span>L</span><span>XL</span></div>
      <div class="row row--cat"><span>Regrowth</span><span class="price">$83</span></div>
      <div class="row row--cat"><span>Full color tint</span><span class="price">$125</span><span class="price">$145</span><span class="price">$165</span><span class="price">$185</span></div>
      <div class="row row--cat"><span>Regrowth lightening</span><span class="price">$165</span><span class="price">$189</span><span class="price">$209</span><span class="price">$229</span></div>
      <div class="row row--cat"><span>Balayage/Ombre</span><span></span><span class="price">$275</span><span class="price">$375</span><span class="price">$475</span></div>
    </div>
    <div class="section" style="top:215px">
      <div class="section__head"><span>Velin Gloss</span></div>
      <div class="row row--cat"><span>Regrowth</span><span class="price">$99</span></div>
      <div class="row row--cat"><span>Full color tint</span><span class="price">$155</span><span class="price">$175</span><span class="price">$195</span><span class="price">$205</span></div>
    </div>
    <div class="section" style="top:288px">
      <div class="section__head"><span>Foils</span></div>
      <div class="row row--cat"><span>Single</span><span class="price">$11</span><span class="price">$13</span><span class="price">$17</span><span class="price">$22</span></div>
      <div class="row row--cat"><span>1/4 Head</span><span class="price">$135</span><span class="price">$155</span><span class="price">$175</span><span class="price">$195</span></div>
      <div class="row row--cat"><span>1/2 Head</span><span class="price">$185</span><span class="price">$205</span><span class="price">$235</span><span class="price">$265</span></div>
      <div class="row row--cat"><span>Full Head</span><span class="price">$235</span><span class="price">$265</span><span class="price">$315</span><span class="price">$355</span></div>
    </div>
    <div class="section" style="top:386px">
      <div class="section__head"><span>Straight</span></div>
      <div class="row row--cat"><span>Keratin straightening system</span><span class="price">$365</span><span class="price">$445</span><span class="price">$535</span><span class="price">$565</span></div>
      <div class="row row--small"><span>Including colour mach &amp; toner</span></div>
      <div class="row row--small"><span>Minimum 6 foils without colour</span></div>
      <div class="row row--small"><span>Minimum change on a Sunday is $40</span></div>
    </div>
  </div>
</section>

</body>
</html>
```